Candle Rental Business seeks new website design

We need a new website design for a Candle hire business. The business rents out pillar candles for events such as weddings and corporate events. Our main target market is weddings. The business name is Lease a Lantern. The business name does not have a logo design.

We would like a website that is light in colours and creates a warm atmosphere. The design needs to be elegant and upmarket. There are different size candles that we hire out, ranging from 10cm diameter to 20cm diameter, flat, tall etc. All our candles are white in colour. Its just the size that differs.

We would also like to include a section for hiring out decor such as glassvases, candlebras, overlays and chairs sachets, chair covers. However, this is not the businesses main focus but an additional offering to customers.

Target Market(s)

Wedding venues and brides. Corporate events. School dances.

Industry/Entity Type

Hospitality

Logo Text

Lease a Lantern

Number of Pages Required

1 page

Font styles to use
Sans Serif
Script

Requirements
Must have
• Pictures of pillar candles. Plain white candles. The website must centre around candles.
Nice to have
• Different examples of candle centrepieces
Should not have
• Pictures must not be of brides. Pictures of surrounding is perferable.

```html
<!DOCTYPE html>
<html lang="en">
<head>
<meta charset="utf-8">
<title>Lease a Lantern – Candles &amp; Decor Hire</title>
<link href="https://fonts.googleapis.com/css2?family=Lato:wght@400;700;900&family=Questrial&display=swap" rel="stylesheet">
<style>
:root{
  --orange:#f07b16;
  --yellow:#fbb217;
  --ink:#2b2b2b;
  --text:#555;
  --muted:#777;
  --light:#ececec;
  --bar:#2a2a2a;
  --white:#fff;
}
*{box-sizing:border-box;margin:0;padding:0}
html,body{width:1200px;height:3046px;overflow:hidden}
body{font-family:"Lato",sans-serif;color:var(--text);background:var(--white);position:relative}
.heading{font-family:"Questrial",sans-serif;font-weight:400;color:var(--ink)}
.btn{display:inline-block;height:38px;line-height:38px;padding:0 26px;font-size:15px;font-family:"Lato",sans-serif;text-decoration:none}
.btn-orange{background:var(--orange);color:var(--white)}
.btn-yellow{background:var(--yellow);color:var(--white)}
.btn-white{background:var(--white);color:var(--orange)}

/* header */
.site-header{position:absolute;top:0;left:0;width:1200px;height:88px;background:var(--white)}
.brand{position:absolute;left:82px;top:14px;display:flex;align-items:center;gap:14px}
.brand-mark{width:56px;height:56px;border-radius:50%;background:#7a8fa0}
.brand-name{font-size:34px;font-weight:700;color:var(--ink)}
.account{position:absolute;right:94px;top:12px;display:flex;gap:36px;font-size:13px;color:var(--muted)}
.account span{display:flex;align-items:center;gap:8px}
.main-nav{position:absolute;right:82px;top:52px;display:flex;gap:46px;font-size:16px;color:var(--ink)}
.main-nav a{color:inherit;text-decoration:none}
.main-nav .active{border:1px solid var(--orange);color:var(--orange);padding:2px 10px;margin-right:-10px;margin-left:-10px;position:relative;top:-3px}

/* hero */
.hero{position:absolute;top:88px;left:0;width:1200px;height:532px;
  background:radial-gradient(ellipse at 50% 30%,#5a3a1d 0%,#2b1a0c 45%,#0e0805 100%)}
.hero-copy{position:absolute;top:280px;width:100%;text-align:center;color:var(--white)}
.hero-title{font-size:40px;font-weight:900;letter-spacing:.3px}
.hero-sub{font-size:30px;font-family:"Lato",sans-serif;margin-top:16px}
.hero .btn{margin-top:26px;height:44px;line-height:44px;font-size:19px;padding:0 16px}

/* about */
.about{position:absolute;top:620px;left:0;width:1200px;height:300px;text-align:center}
.about h2{font-size:40px;margin-top:52px}
.about p{width:1020px;margin:18px auto 0;font-size:14px;line-height:26px;color:var(--muted)}
.about .btn{margin-top:20px}

/* hire candles */
.feature{position:absolute;top:920px;left:0;width:1200px;height:473px;display:flex}
.feature-photo{width:600px;height:100%;background:linear-gradient(135deg,#6c6a58 0%,#8f8a72 40%,#4d4a3c 75%,#2c2a22 100%)}
.feature-body{width:600px;height:100%;background:var(--orange);color:var(--white);padding:36px 56px 0 56px}
.round-icon{width:60px;height:60px;border:2px solid var(--white);border-radius:50%;display:flex;align-items:center;justify-content:center}
.feature-body h2{font-size:40px;font-weight:700;margin-top:14px}
.feature-body p{font-size:14px;line-height:29px;margin-top:12px;width:460px}
.btn-row{display:flex;gap:6px;margin-top:28px}

/* two panels */
.panels{position:absolute;top:1393px;left:0;width:1200px;height:471px;display:flex}
.panel{width:600px;height:100%;position:relative}
.panel-candles{background:linear-gradient(120deg,#5a3c22 0%,#2a1c12 50%,#18100b 100%)}
.panel-decor{background:linear-gradient(150deg,#3a2212 0%,#8a5a2a 50%,#c98c44 100%)}
.panel-box{position:absolute;top:36px;bottom:36px;color:var(--white);text-align:center;padding-top:68px}
.panel-candles .panel-box{left:46px;right:32px;background:rgba(40,28,20,.6)}
.panel-decor .panel-box{left:40px;right:58px;background:rgba(240,123,22,.85)}
.panel-box .round-icon{margin:0 auto}
.panel-box h2{font-size:40px;font-weight:700;margin-top:10px}
.panel-box p{font-size:14px;line-height:29px;margin:10px auto 0;width:430px}
.panel-box .btn-row{justify-content:center;margin-top:20px}

/* how it works */
.how{position:absolute;top:1864px;left:0;width:1200px;height:450px;text-align:center}
.how h2{font-size:40px;margin-top:46px}
.step{position:absolute;top:171px;width:200px;text-align:center}
.step-circle{width:150px;height:150px;border-radius:50%;margin:0 auto;display:flex;align-items:center;justify-content:center}
.step-orange{background:var(--orange)}
.step-yellow{background:var(--yellow)}
.step-label{font-family:"Questrial",sans-serif;font-size:21px;line-height:28px;color:var(--muted);margin-top:20px}
.flow-arrow{position:absolute}

/* decor hires */
.decor{position:absolute;top:2314px;left:0;width:1200px;height:392px;background:var(--light);text-align:center}
.decor h2{font-size:40px;margin-top:44px}
.decor-grid{position:absolute;top:154px;left:81px;display:flex;gap:10px}
.decor-tile{width:252px;height:187px;position:relative;display:flex;align-items:center;justify-content:center}
.decor-tile::after{content:"";position:absolute;inset:10px;border:2px solid rgba(255,255,255,.85)}
.decor-tile span{position:relative;z-index:1;color:var(--white);font-size:22px;font-weight:700;line-height:30px}
.tile-vases{background:linear-gradient(135deg,#3a2412,#7a4a20 55%,#2a1a0e)}
.tile-displays{background:linear-gradient(135deg,#4a463a,#8a8670 55%,#3a3a2e)}
.tile-overlays{background:linear-gradient(135deg,#bfbab0,#8e8a80 55%,#6e6a62)}
.tile-covers{background:linear-gradient(135deg,#d8b8c0,#b88a98 55%,#8e6a74)}

/* footer */
.site-footer{position:absolute;top:2706px;left:0;width:1200px;height:284px;background:var(--light)}
.site-footer::before{content:"";position:absolute;left:81px;right:58px;top:0;height:1px;background:#d2d2d2}
.foot-col{position:absolute;top:34px}
.foot-col h3{font-size:14px;font-weight:700;color:#444;font-family:"Lato",sans-serif}
.quick-links{left:81px}
.quick-links ul{list-style:none;margin-top:16px}
.quick-links li{font-size:12px;color:var(--muted);line-height:33px;padding-left:18px;position:relative}
.quick-links li::before{content:"";position:absolute;left:0;top:15px;width:4px;height:4px;border-radius:50%;background:#999}
.contact{left:305px}
.contact-row{display:flex;gap:12px;margin-top:16px;font-size:13px;color:var(--muted);line-height:18px;align-items:flex-start}
.contact-row svg{flex:none;margin-top:2px}
.inquiry{left:652px;width:240px}
.field{border:1px solid #888;background:var(--white);height:34px;margin-top:8px;font-size:11px;color:var(--muted);padding:8px 6px}
.inquiry .field:first-of-type{margin-top:14px}
.field-msg{height:78px}
.submit{margin-top:6px;background:var(--orange);color:var(--white);height:34px;line-height:34px;text-align:center;font-size:14px}
.follow{left:1003px}
.social{display:flex;align-items:center;gap:12px;margin-top:10px;font-size:12px;color:#4a7bb8}
.social:first-of-type{margin-top:14px}
.social i{width:30px;height:30px;border-radius:50%;display:block}
.bottom-bar{position:absolute;top:2990px;left:0;width:1200px;height:56px;background:var(--bar);color:#cfcfcf;font-size:13px}
.bottom-bar .copy{position:absolute;left:81px;top:20px}
.bottom-bar .pay{position:absolute;right:78px;top:17px;display:flex;align-items:center;gap:6px}
.pay b{font-weight:400;margin-right:14px}
.card{width:28px;height:20px;background:#d9d9d9;border-radius:2px}
</style>
</head>
<body>

<header class="site-header">
  <div class="brand">
    <div class="brand-mark"></div>
    <div class="brand-name">Lease a Lantern</div>
  </div>
  <div class="account">
    <span><svg width="14" height="14" viewBox="0 0 14 14"><rect x="4" y="1" width="9" height="12" fill="none" stroke="#777"/><path d="M1 7h7M5 4l3 3-3 3" fill="none" stroke="#777"/></svg>log In</span>
    <span><svg width="14" height="14" viewBox="0 0 14 14"><rect x="1" y="1" width="12" height="12" fill="none" stroke="#777"/><path d="M4 5h6M4 8h6" stroke="#777"/></svg>Register</span>
  </div>
  <nav class="main-nav">
    <a class="active" href="#">Home</a>
    <a href="#">About Us</a>
    <a href="#">Our Products</a>
    <a href="#">Contact Us</a>
  </nav>
</header>

<section class="hero" role="img" aria-label="Candelabras with tall white pillar candles above a set banquet table">
  <div class="hero-copy">
    <div class="hero-title">There Are Two Ways of Spreading Light:</div>
    <div class="hero-sub">To Be The Candle Or The Mirror That Reflects It</div>
    <a class="btn btn-orange" href="#">Rent Candles Now</a>
  </div>
</section>

<section class="about">
  <h2 class="heading">About Us</h2>
  <p>We are a family owned and operated company and began making decorative candles for all occasions.&nbsp; All of our candles are individually hand made in our candle studio, situated in Harbourvale, outside Northport.&nbsp; Our wax is local and of a very high quality, and dripless! Our wax is also made with a high melting point, which means it will not melt or bend in hot temperatures.</p>
  <a class="btn btn-orange" href="#">Read More</a>
</section>

<section class="feature">
  <div class="feature-photo" role="img" aria-label="White pillar candles on tall stands with green floral centrepieces"></div>
  <div class="feature-body">
    <div class="round-icon"><svg width="26" height="30" viewBox="0 0 26 30"><path d="M13 1c3 4 3 6 0 8-3-2-3-4 0-8z" fill="#fff"/><rect x="8" y="11" width="10" height="14" fill="#fff"/><rect x="4" y="26" width="18" height="3" fill="#fff"/></svg></div>
    <h2>Hire Candles</h2>
    <p>Do you love using candles for your events but tired of sorting old used candles or buying expensive candles. Believe it or not you can now rent candles.&nbsp; All our candles come in different sizes and heights. You can add the ambience of candlelight to your event of wedding ceremony without the worry over dripping wax or open candle flames. Our candles do not melt.</p>
    <div class="btn-row"><a class="btn btn-white" href="#">Buy Now</a><a class="btn btn-yellow" href="#">More Info</a></div>
  </div>
</section>

<section class="panels">
  <div class="panel panel-candles" role="img" aria-label="Pillar candles in glass holders on a dark dinner table">
    <div class="panel-box">
      <div class="round-icon"><svg width="26" height="30" viewBox="0 0 26 30"><path d="M13 1c3 4 3 6 0 8-3-2-3-4 0-8z" fill="#fff"/><rect x="6" y="11" width="14" height="17" fill="#fff"/></svg></div>
      <h2>Personalised Candles</h2>
      <p>Lease a Lantern provides the opportunity to give a thoughtful, meaningful gift at a friendly price point. This unique gift conveys the time and care you put into creating it. The recipient will enjoy the beautiful presentation and be reminded...</p>
      <div class="btn-row"><a class="btn btn-orange" href="#">Buy Now</a><a class="btn btn-yellow" href="#">More Info</a></div>
    </div>
  </div>
  <div class="panel panel-decor" role="img" aria-label="Warm glowing candles in glass vases on an event table">
    <div class="panel-box">
      <div class="round-icon"><svg width="30" height="30" viewBox="0 0 30 30"><rect x="4" y="12" width="6" height="12" fill="#fff"/><rect x="12" y="8" width="6" height="16" fill="#fff"/><rect x="20" y="12" width="6" height="12" fill="#fff"/><rect x="3" y="25" width="24" height="3" fill="#fff"/></svg></div>
      <h2>Décor Hire</h2>
      <p>Lease a Lantern provides the opportunity to give a thoughtful, meaningful gift at a friendly price point. This unique gift conveys the time and care you put into creating it. The recipient will enjoy the beautiful presentation and be reminded...</p>
      <div class="btn-row"><a class="btn btn-white" href="#">Buy Now</a><a class="btn btn-yellow" href="#">More Info</a></div>
    </div>
  </div>
</section>

<section class="how">
  <h2 class="heading">How It Works</h2>
  <svg class="flow-arrow" style="left:250px;top:120px" width="110" height="40" viewBox="0 0 110 40"><path d="M4 30Q50 0 100 20" fill="none" stroke="#ddd" stroke-width="4"/><path d="M90 8l12 12-16 4" fill="none" stroke="#ddd" stroke-width="4"/></svg>
  <svg class="flow-arrow" style="left:550px;top:270px" width="110" height="40" viewBox="0 0 110 40"><path d="M4 10Q50 40 100 20" fill="none" stroke="#ddd" stroke-width="4"/><path d="M86 14l16 6-12 12" fill="none" stroke="#ddd" stroke-width="4"/></svg>
  <svg class="flow-arrow" style="left:846px;top:120px" width="110" height="40" viewBox="0 0 110 40"><path d="M4 30Q50 0 100 20" fill="none" stroke="#ddd" stroke-width="4"/><path d="M90 8l12 12-16 4" fill="none" stroke="#ddd" stroke-width="4"/></svg>

  <div class="step" style="left:54px">
    <div class="step-circle step-orange"><svg width="50" height="70" viewBox="0 0 50 70"><path d="M25 2c6 8 6 12 0 16-6-4-6-8 0-16z" fill="#fff"/><rect x="10" y="22" width="30" height="44" rx="3" fill="#fff"/><path d="M10 36h30M10 50h30" stroke="#f07b16" stroke-width="3"/></svg></div>
    <div class="step-label">Choose your<br>Candle</div>
  </div>
  <div class="step" style="left:351px">
    <div class="step-circle step-yellow"><svg width="56" height="70" viewBox="0 0 56 70"><rect x="16" y="4" width="10" height="36" rx="5" fill="#fff"/><path d="M16 30h32v24a12 12 0 0 1-12 12H26a10 10 0 0 1-10-10z" fill="#fff"/><rect x="4" y="34" width="12" height="8" rx="4" fill="#fff" transform="rotate(30 10 38)"/></svg></div>
    <div class="step-label">Book your<br>Candle</div>
  </div>
  <div class="step" style="left:649px">
    <div class="step-circle step-orange"><svg width="76" height="56" viewBox="0 0 76 56"><rect x="8" y="4" width="62" height="36" fill="#fff" transform="rotate(-12 38 22)"/><rect x="4" y="16" width="66" height="36" fill="#fff" stroke="#f07b16" stroke-width="3"/><rect x="11" y="22" width="52" height="24" fill="none" stroke="#f07b16" stroke-width="2"/><circle cx="37" cy="34" r="8" fill="#f07b16"/></svg></div>
    <div class="step-label">Make<br>payment</div>
  </div>
  <div class="step" style="left:945px">
    <div class="step-circle step-yellow"><svg width="60" height="76" viewBox="0 0 60 76"><path d="M30 2c6 8 6 12 0 16-6-4-6-8 0-16z" fill="#fff"/><rect x="20" y="22" width="20" height="36" fill="none" stroke="#fff" stroke-width="4"/><path d="M4 60h52l-6 8H10z" fill="#fff"/></svg></div>
    <div class="step-label">Light Up<br>Your Event</div>
  </div>
</section>

<section class="decor">
  <h2 class="heading">Other Decor Hires</h2>
  <div class="decor-grid">
    <div class="decor-tile tile-vases" role="img" aria-label="Candles in glass vases"><span>Glass Vases</span></div>
    <div class="decor-tile tile-displays" role="img" aria-label="Pillar candle display stands"><span>Displays</span></div>
    <div class="decor-tile tile-overlays" role="img" aria-label="Table overlays and chair sashes"><span>Overlays &amp;<br>Chairs Sachets</span></div>
    <div class="decor-tile tile-covers" role="img" aria-label="Pink chair covers with bows"><span>Chair Covers</span></div>
  </div>
</section>

<footer class="site-footer">
  <div class="foot-col quick-links">
    <h3>Quick Links</h3>
    <ul><li>Home</li><li>About Us</li><li>Our Products</li><li>Contact Us</li></ul>
  </div>
  <div class="foot-col contact">
    <h3>Contact Details</h3>
    <div class="contact-row"><svg width="18" height="22" viewBox="0 0 18 22"><path d="M9 1a7 7 0 0 1 7 7c0 5-7 13-7 13S2 13 2 8a7 7 0 0 1 7-7z" fill="none" stroke="#777" stroke-width="2"/><circle cx="9" cy="8" r="2.5" fill="#777"/></svg><span>1/23 Lorem Ips Dolo, Consecer<br>wererr Nonuy - 12345</span></div>
    <div class="contact-row"><svg width="18" height="20" viewBox="0 0 18 20"><path d="M4 1l4 4-2 3c1 3 3 5 6 6l3-2 3 4-3 3C8 18 1 11 1 4z" fill="none" stroke="#777" stroke-width="2"/></svg><span>123-456-7890</span></div>
    <div class="contact-row"><svg width="18" height="14" viewBox="0 0 18 14"><rect x="1" y="1" width="16" height="12" fill="none" stroke="#777" stroke-width="2"/><path d="M1 1l8 7 8-7" fill="none" stroke="#777" stroke-width="2"/></svg><span>info@companyname.com</span></div>
  </div>
  <div class="foot-col inquiry">
    <h3>Quick Inquiry</h3>
    <div class="field">Name</div>
    <div class="field">Phone</div>
    <div class="field field-msg">Message</div>
    <div class="submit">Submit</div>
  </div>
  <div class="foot-col follow">
    <h3>Follow Us</h3>
    <div class="social"><i style="background:#3b5a98"></i>Fanpage</div>
    <div class="social"><i style="background:#3aa8e0"></i>Chirper</div>
    <div class="social"><i style="background:#1a7fbc"></i>ProNet</div>
    <div class="social"><i style="background:#d24a3a"></i>CirclePlus</div>
  </div>
</footer>

<div class="bottom-bar">
  <div class="copy">Copyright © 2016 Lease a Lantern. All Rights Reserved.</div>
  <div class="pay"><b>We Accept:</b><span class="card"></span><span class="card"></span><span class="card"></span><span class="card"></span></div>
</div>

</body>
</html>
```